Business Card Design Project

I need business cards communicate a high end look and cutting edge sophistication,creativity, with a logo branding.
The company name is: Keystone Crafters we specialize in Remodel ing and Design of Resindental and Commercial our company is based in Los Angeles Ca our clients are high end high dollar . The design should communicate the statements above.
Updates
I would like to see both side the business card
Industry/Entity Type
Business
Requirements
Nice to have
- Maybe a design with a faint Blueprint /construction floor plan background, maybe

```html
<!DOCTYPE html>
<html lang="en">
<head>
<meta charset="utf-8">
<title>Keystone Crafters — Business Card</title>
<link rel="stylesheet" href="https://fonts.googleapis.com/css2?family=PT+Sans:wght@400;700&family=Source+Sans+3:wght@600;700&family=Bitter:wght@600&display=swap">
<style>
  :root {
    --page-bg: #e9e9e7;
    --card-blue: #0b3ce6;
    --band-blue: #0a43f0;
    --card-grey: #808080;
    --brand-red: #c4111d;
    --white: #ffffff;
    --ink: #111111;
  }
  * { margin: 0; padding: 0; box-sizing: border-box; }
  html, body { width: 939px; height: 1200px; overflow: hidden; }
  body { background: var(--page-bg); position: relative; font-family: "PT Sans", sans-serif; }

  .card {
    position: absolute;
    left: 133px;
    width: 672px;
    height: 383px;
    border-radius: 13px;
    overflow: hidden;
    box-shadow: 0 4px 14px rgba(0,0,0,0.18);
  }
  .card--front { top: 133px; }
  .card--back { top: 683px; }

  .card__plan { position: absolute; inset: 0; }
  .card--front .card__plan { background: linear-gradient(160deg, #1348f0 0%, var(--card-blue) 55%, #0934d2 100%); }
  .card--back .card__plan { background: linear-gradient(160deg, #888 0%, var(--card-grey) 55%, #737373 100%); }

  .brand-band {
    position: absolute;
    left: 0; top: 80px;
    width: 353px; height: 76px;
    background: var(--brand-red);
    display: flex; align-items: center;
    padding-left: 28px;
  }
  .brand-name {
    font-family: "Source Sans 3", sans-serif;
    font-weight: 700;
    font-size: 38px;
    letter-spacing: -0.6px;
    color: var(--white);
    white-space: nowrap;
  }
  .tagline {
    position: absolute;
    left: 28px; top: 171px;
    font-family: "Source Sans 3", sans-serif;
    font-weight: 700;
    font-size: 15.5px;
    line-height: 19px;
    color: var(--white);
    letter-spacing: -0.2px;
  }
  .name-box {
    position: absolute;
    left: 421px; top: 87px;
    width: 251px; height: 71px;
    background: var(--white);
    padding: 14px 0 0 16px;
    color: var(--ink);
  }
  .person-name {
    font-family: "Bitter", serif;
    font-weight: 600;
    font-size: 22px;
    line-height: 24px;
  }
  .person-title { font-size: 17px; line-height: 20px; }

  .contact {
    position: absolute;
    left: 437px; top: 258px;
    font-size: 15.5px;
    line-height: 20px;
    color: var(--white);
    font-style: normal;
  }

  .url-band {
    position: absolute;
    left: 0; top: 81px;
    width: 100%; height: 76px;
    background: var(--band-blue);
    display: flex; align-items: center;
    padding-left: 28px;
  }
  .url {
    font-family: "Source Sans 3", sans-serif;
    font-weight: 700;
    font-size: 35px;
    letter-spacing: -0.4px;
    color: var(--white);
  }
</style>
</head>
<body>
  <section class="card card--front">
    <div class="card__plan" role="img" aria-label="Faint architectural floor plan drawing of a house in white lines on blue"></div>
    <div class="brand-band"><span class="brand-name">Keystone Crafters</span></div>
    <p class="tagline">Remodeling and Design of<br>Residential and Commercial Properties</p>
    <div class="name-box">
      <p class="person-name">Marcus Whitfield</p>
      <p class="person-title">president</p>
    </div>
    <address class="contact">
      4410 Cedarline Blvd<br>
      Suite# 1200<br>
      Los Angeles, CA 90036<br>
      323-555-0147<br>
      marcus@keystonecrafters.net
    </address>
  </section>

  <section class="card card--back">
    <div class="card__plan" role="img" aria-label="Architectural floor plan drawing of a house in white lines on grey"></div>
    <div class="url-band"><span class="url">www.keystonecrafters.net</span></div>
  </section>
</body>
</html>
```